QM Fenwold Detailing, Inc.

I'm looking for business card design for an existing company with an existing logo/website. www.qmfenwold-detailing.com. VETERAN OWNED logo must be present.

Target Market(s)

Structural and architectural steel fabricators

Industry/Entity Type

Structural and architectural steel detailing and engineering

Contact Information for Business Card

logo, business name, address, phone, website, email, employee info

Font styles to use
Serif

Colors
00AB8E
00BBA5
67D7C9
C6EFE9
E9F9F6

Requirements
Must have
• company logo, website, VETERAN OWNED LOGO
Should not have
• Don't make it too busy. Less is more

```html
<!DOCTYPE html>
<html lang="en">
<head>
<meta charset="utf-8">
<title>QM Fenwold Detailing, Inc. – Business Card</title>
<link href="https://fonts.googleapis.com/css2?family=Lora:wght@400;600;700&family=Source+Serif+4:wght@400;600&display=swap" rel="stylesheet">
<style>
  :root{
    --bg:#2c2e33;
    --teal:#2a8f96;
    --teal-light:#c6efe9;
    --ink:#111111;
    --band:#1d1d1d;
    --grey:#cfcfcf;
    --paper:#ffffff;
    --muted:#444444;
  }
  html,body{margin:0;padding:0;width:1200px;height:900px;overflow:hidden;background:var(--bg);}
  .stage{position:relative;width:1200px;height:900px;}
  .card{position:absolute;left:320px;width:560px;height:320px;border-radius:22px;overflow:hidden;}
  .card--front{top:90px;background:var(--paper);}
  .card--back{top:480px;background:var(--teal);}

  .front__heading{position:absolute;left:0;right:0;top:36px;margin:0;text-align:center;white-space:nowrap;
    font:400 38px/1 "Lora",serif;letter-spacing:1px;color:var(--ink);}
  .person{position:absolute;left:20px;top:134px;width:176px;text-align:right;white-space:nowrap;}
  .person__name{margin:0;font:700 20px/1.1 "Lora",serif;color:var(--teal);}
  .person__title{margin:5px 0 0;font:400 12px/1.2 "Source Serif 4",serif;color:var(--muted);}
  .divider{position:absolute;left:206px;top:128px;width:1px;height:70px;background:var(--teal);}
  .contacts{position:absolute;left:220px;top:130px;margin:0;padding:0;list-style:none;
    font:400 13px/1 "Source Serif 4",serif;color:var(--ink);}
  .contacts li{display:flex;align-items:center;gap:8px;height:22px;white-space:nowrap;}
  .contacts svg{width:12px;height:12px;fill:var(--teal);flex:none;}

  .veteran-badge{position:absolute;right:26px;top:136px;width:56px;height:56px;border-radius:50%;
    background:var(--teal-light);border:2px solid var(--teal);box-sizing:border-box;}

  .footer-band{position:absolute;left:0;bottom:0;width:560px;height:56px;}
  .footer-band__dark{position:absolute;left:0;top:0;width:330px;height:56px;background:var(--band);}
  .footer-band__teal{position:absolute;left:0;top:0;width:560px;height:56px;}
  .address{position:absolute;left:24px;bottom:0;height:56px;display:flex;align-items:center;white-space:nowrap;
    font:400 13px/1 "Source Serif 4",serif;color:var(--grey);}
  .front__mark{position:absolute;right:24px;bottom:0;height:56px;display:flex;align-items:center;gap:8px;white-space:nowrap;
    font:600 16px/1 "Lora",serif;color:var(--paper);}
  .mark-square{width:12px;height:12px;background:var(--paper);}

  .back__mark{position:absolute;left:0;right:0;top:104px;display:flex;justify-content:center;align-items:center;gap:14px;
    font:600 44px/1 "Lora",serif;color:var(--paper);white-space:nowrap;}
  .back__mark .mark-square{width:26px;height:26px;}
  .back__name{position:absolute;left:0;right:0;top:180px;margin:0;text-align:center;white-space:nowrap;
    font:400 26px/1 "Lora",serif;letter-spacing:2px;color:var(--ink);}
</style>
</head>
<body>
<main class="stage">
  <section class="card card--front" aria-label="Business card front">
    <h1 class="front__heading">FENWOLD DETAILING</h1>
    <div class="person">
      <p class="person__name">Daniel Harrow</p>
      <p class="person__title">Managing Director</p>
    </div>
    <div class="divider"></div>
    <ul class="contacts">
      <li><svg viewBox="0 0 24 24" aria-hidden="true"><path d="M6.6 10.8a15 15 0 0 0 6.6 6.6l2.2-2.2c.3-.3.7-.4 1-.2 1.1.4 2.3.6 3.6.6.6 0 1 .4 1 1V20c0 .6-.4 1-1 1A17 17 0 0 1 3 4c0-.6.4-1 1-1h3.5c.6 0 1 .4 1 1 0 1.3.2 2.5.6 3.6.1.3 0 .7-.2 1z"/></svg>555.014.2290</li>
      <li><svg viewBox="0 0 24 24" aria-hidden="true"><path d="M2 5h20v14H2zm2 2v.5l8 5 8-5V7l-8 5z"/></svg>info@qmfenwold-detailing.com</li>
      <li><svg viewBox="0 0 24 24" aria-hidden="true"><path d="M12 2a10 10 0 1 0 0 20 10 10 0 0 0 0-20zm6.9 9h-3a15 15 0 0 0-1.3-6A8 8 0 0 1 18.9 11zM12 4c.9 1.3 1.7 3.9 1.9 7h-3.8c.2-3.1 1-5.7 1.9-7zM9.4 5a15 15 0 0 0-1.3 6h-3A8 8 0 0 1 9.4 5zM5.1 13h3a15 15 0 0 0 1.3 6A8 8 0 0 1 5.1 13zM12 20c-.9-1.3-1.7-3.9-1.9-7h3.8c-.2 3.1-1 5.7-1.9 7zm2.6-1a15 15 0 0 0 1.3-6h3a8 8 0 0 1-4.3 6z"/></svg>www.qmfenwold-detailing.com</li>
    </ul>
    <div class="veteran-badge" role="img" aria-label="Veteran owned badge"></div>
    <div class="footer-band">
      <svg class="footer-band__teal" viewBox="0 0 560 56" aria-hidden="true"><polygon points="330,0 560,0 560,56 300,56" fill="var(--teal)"/></svg>
      <div class="footer-band__dark"></div>
      <span class="address">240 Cedar Ridge Lane Brandon, TX 75001</span>
      <span class="front__mark"><span class="mark-square"></span>QM Fenwold</span>
    </div>
  </section>

  <section class="card card--back" aria-label="Business card back">
    <div class="back__mark"><span class="mark-square"></span>QM Fenwold</div>
    <p class="back__name">FENWOLD DETAILING</p>
  </section>
</main>
</body>
</html>
```